Buch-Cover für Funkenflug gesucht
Zielgruppe
Wir sind eine Firma die hochwertige Fitnessprodukte produziert und vertreibt. Unsere Zielgruppe sind gesundheitsbewusste Frauen ab Mitte 20 bis open end, die hohe Ansprüche an sich selbst stellen und sich für das Thema Selbstoptimierung interessieren.
Aufgabenstellung
Es soll ein Hardcover gestaltet werden.
Buchtitel: Funkenflug, Untertitel: Kleine Lichter am Meer
Detaillierte Beschreibung der Projektanforderungen siehe Anhang Projektbeschreibung. Darüber hinaus bin ich auch für alternative Gestaltungs-Ideen offen.
Das Design soll der Käuferin folgendes vermitteln:
- Wertigkeit
- Positivität
und sie ein bisschen träumen lassen und natürlich neugierig auf den Inhalt machen.

```html
<!DOCTYPE html>
<html lang="de">
<head>
<meta charset="utf-8">
<title>Funkenflug – Buchumschlag</title>
<link rel="stylesheet" href="https://fonts.googleapis.com/css2?family=Great+Vibes&family=Antonio:wght@500&family=Carlito&family=Lobster+Two:ital,wght@1,700&family=Berkshire+Swash&family=Montserrat:wght@800&display=swap">
<style>
  :root {
    --page: #ffffff;
    --night: #1c3f7a;
    --dusk: #7a5a86;
    --glow: #f3d59a;
    --teal: #1a8b8a;
    --teal-deep: #11706f;
    --teal-bright: #17a3a4;
    --peach: #f1d2b8;
    --ink-light: #fdf4e6;
    --rust: #c9582a;
    --spine-yellow: #f4d35e;
    --car-shadow: #3b3a4a;
  }
  * { box-sizing: border-box; margin: 0; padding: 0; }
  html, body { width: 1200px; height: 1194px; overflow: hidden; background: var(--page); }
  .canvas { position: relative; width: 1200px; height: 1194px; }

  .spread {
    position: absolute; left: 40px; top: 220px;
    width: 1120px; height: 754px;
    display: flex;
    box-shadow: 8px 8px 14px rgba(0,0,0,.35);
  }

  /* Back cover */
  .back {
    position: relative; width: 546px; height: 100%;
    background:
      radial-gradient(ellipse 260px 200px at 48% 30%, rgba(243,213,154,.9), rgba(243,213,154,0) 75%),
      linear-gradient(180deg, var(--night) 0%, var(--dusk) 20%, #9c8a6e 36%, #4f8f86 52%, var(--teal) 70%, var(--teal-deep) 100%);
  }
  .back-title {
    position: absolute; top: 100px; width: 100%; text-align: center;
    font-family: "Great Vibes", cursive; font-size: 86px; color: #fff;
    text-shadow: 0 0 14px rgba(255,230,180,.8);
  }
  .back-heading {
    position: absolute; top: 332px; width: 100%; text-align: center;
    font-family: "Antonio", sans-serif; font-weight: 500; font-size: 30px;
    letter-spacing: 4px; color: var(--ink-light);
  }
  .back-copy {
    position: absolute; top: 372px; left: 44px; width: 460px;
    font-family: "Carlito", sans-serif; font-size: 14.6px; line-height: 21px;
    color: var(--ink-light); text-align: justify;
  }
  .back-copy p + p { margin-top: 20px; }

  /* Spine */
  .spine {
    position: relative; width: 42px; height: 100%;
    background: linear-gradient(180deg, #1d7e86, var(--teal) 40%, var(--teal-deep));
    display: flex; flex-direction: column; align-items: center; padding-top: 18px;
  }
  .spine span { writing-mode: vertical-rl; white-space: nowrap; }
  .spine-author { font-family: "Lobster Two", cursive; font-style: italic; font-weight: 700; font-size: 16px; color: #fff; }
  .spine-title { margin-top: 14px; font-family: "Montserrat", sans-serif; font-weight: 800; font-size: 26px; letter-spacing: 2px; color: #f2f2f2; }
  .spine-subtitle { margin-top: 10px; font-family: "Berkshire Swash", cursive; font-size: 21px; color: var(--spine-yellow); }

  /* Front cover */
  .front {
    position: relative; width: 532px; height: 100%; overflow: hidden;
    background: linear-gradient(180deg, #1e4d86 0%, #4c8b9a 14%, #d9c7ad 30%, var(--peach) 44%, #e6c3a8 52%, #8a8692 62%, var(--car-shadow) 100%);
  }
  .front-scene {
    position: absolute; left: 0; right: 0; top: 405px; bottom: 0;
    background: linear-gradient(180deg, #6d6775 0%, #a99b86 25%, #5b5563 55%, #2f2e3a 100%);
  }
  .publisher {
    position: absolute; top: 38px; width: 100%; text-align: center;
    font-family: "Lobster Two", cursive; font-style: italic; font-weight: 700;
    font-size: 22px; color: #2f6fd0;
  }
  .front-author {
    position: absolute; top: 84px; width: 100%; text-align: center;
    font-family: "Lobster Two", cursive; font-style: italic; font-weight: 700;
    font-size: 34px; color: #fff; text-shadow: 2px 2px 3px rgba(0,0,0,.35);
  }
  .front-title {
    position: absolute; top: 135px; width: 100%; text-align: center;
    font-family: "Great Vibes", cursive; font-size: 132px; line-height: 1;
    color: var(--teal-bright); text-shadow: 2px 2px 0 #fff, 4px 5px 6px rgba(0,0,0,.25);
  }
  .front-subtitle {
    position: absolute; top: 300px; width: 100%; text-align: center;
    font-family: "Berkshire Swash", cursive; font-size: 28px; line-height: 32px;
    color: var(--rust);
  }
</style>
</head>
<body>
<div class="canvas">
  <div class="spread">
    <section class="back" role="img" aria-label="Abendhimmel mit warmen Lichtpunkten, übergehend in Türkis">
      <h2 class="back-title">Funkenflug</h2>
      <h3 class="back-heading">Was zählt wirklich?</h3>
      <div class="back-copy">
        <p>Ich habe mich oft gefragt: Wie soll ich bloß die Liebe und Bestätigung, die mir damals in meiner Kindheit verwehrt blieben, "nachholen"? Lösungsansätze für mein Problem hatte in der Vergangenheit durchaus: Ich versuchte das Loch mit Hilfe zur Selbsthilfe, Erfolg im Job und Konsum zu stopfen. Und meine Partner mussten auch für so einiges herhalten.</p>
        <p>Von Gott wollte ich lange nichts wissen. Schließlich hatte er es zugelassen, dass mir sehr viel Unheil in meinem Leben widerfahren ist. Und deshalb war ich echt wütend auf ihn.</p>
        <p>Heutzutage bin ich mir sicher, dass ich mit dieser Denkweise meine Lebenszeit verschwendet habe. Letzten Sommer begriff ich endlich: im Leben gilt die gleiche Gesetzmäßigkeit wie beim Autofahren. Der Rückspiegel ist so klein und die Frontscheibe so groß, weil das, was vor uns liegt, viel wichtiger ist als das, was hinter uns liegt. Aufgrund dieser Erkenntnis entschied ich mich, einen völlig neuen Weg einzuschlagen und wagte mich auf eine spannende Reise, die mein Leben für immer veränderte ...</p>
      </div>
    </section>

    <section class="spine">
      <span class="spine-author">Mareike Tessendorf</span>
      <span class="spine-title">FUNKENFLUG</span>
      <span class="spine-subtitle">Kleine Lichter am Meer</span>
    </section>

    <section class="front" role="img" aria-label="Sonnenuntergangshimmel mit Lichtreflexen über einem offenen Cabrio auf einem Feldweg">
      <div class="front-scene" role="img" aria-label="Blick von hinten in ein Cabrio, Fahrerin am Steuer, Weg durch Dünenlandschaft"></div>
      <div class="publisher">Lumenwerk</div>
      <div class="front-author">Mareike Tessendorf</div>
      <h1 class="front-title">Funkenflug</h1>
      <p class="front-subtitle">Kleine Lichter<br>am Meer</p>
    </section>
  </div>
</div>
</body>
</html>
```